Stationary Design Letterhead and Envelope

Artist should provide Letterhead and envelop stationary designs

Info for stationary:
Fernhallow Outdoor Advertising
4873 Quarry Rd. 915 N. PO BOX 528617
Austin, TX 78519

Dale Fernhallow
President
555-862-1907
dale@fernhallowsigns.example
fernhallowsigns.example

Target Market(s)

clients

Colors
0054AA
0677BA
7BADD7
CADEEF
E8F1F8

Requirements
Must have
• high quality unique eye catching and dynamic

```html
<!DOCTYPE html>
<html lang="en">
<head>
<meta charset="utf-8">
<title>Fernhallow Outdoor Advertising — Stationery</title>
<link rel="stylesheet" href="https://fonts.googleapis.com/css2?family=Montserrat:wght@700&family=Questrial&family=Roboto:wght@400&display=swap">
<style>
  :root {
    --brand-blue: #0677BA;
    --brand-blue-deep: #0054AA;
    --brand-tint: #E8F1F8;
    --ink: #111111;
    --text: #555555;
    --paper: #f6f6f6;
    --backdrop: #2b2b2b;
  }
  * { box-sizing: border-box; margin: 0; padding: 0; }
  html, body { width: 1200px; height: 837px; overflow: hidden; }
  body {
    position: relative;
    background: var(--backdrop);
    font-family: "Questrial", sans-serif;
    color: var(--text);
  }
  .sheet { position: absolute; background: var(--paper); }

  /* Wordmark */
  .wordmark { position: absolute; font-family: "Montserrat", sans-serif; font-weight: 700; color: var(--brand-blue); line-height: 1; text-transform: uppercase; }
  .wordmark .name { display: block; font-size: 19px; letter-spacing: 0.2px; }
  .wordmark .tag { display: block; font-size: 7px; letter-spacing: 0.6px; margin-top: 3px; }
  .wordmark.small .name { font-size: 14px; }
  .wordmark.small .tag { font-size: 5.2px; margin-top: 2px; }
  .wordmark.on-dark { color: #ffffff; }

  /* Letterhead */
  .letterhead { left: 73px; top: 61px; width: 503px; height: 708px; }
  .letterhead .wordmark { left: 44px; top: 52px; }
  .salutation { position: absolute; left: 44px; top: 198px; font-size: 13px; color: #444; }
  .letter-body { position: absolute; left: 44px; top: 236px; width: 418px; font-size: 7.4px; line-height: 10.9px; text-align: justify; }
  .letter-body p { margin-bottom: 10.9px; }
  .closing { position: absolute; left: 44px; top: 464px; font-size: 7.4px; }
  .signature { position: absolute; left: 41px; top: 494px; width: 89px; height: 38px; background: var(--brand-tint); border-radius: 3px; }

  /* Footer rule + contact */
  .rule { position: absolute; height: 3px; display: flex; }
  .rule .blue { background: var(--brand-blue); flex: 0 0 auto; }
  .rule .black { background: var(--ink); flex: 1; clip-path: polygon(2px 0, 100% 0, 100% 100%, 0 100%); margin-left: -1px; }
  .contact { position: absolute; font-family: "Roboto", sans-serif; font-size: 7.4px; line-height: 10px; color: #555; }
  .contact li { list-style: none; display: flex; align-items: center; gap: 4px; }
  .contact svg { width: 7px; height: 7px; fill: var(--brand-blue); }
  .address { position: absolute; font-family: "Roboto", sans-serif; font-size: 7.4px; line-height: 10px; text-align: right; color: #555; }
  .address .company { color: var(--brand-blue); }

  /* Envelopes */
  .envelope-back { left: 629px; top: 164px; width: 506px; height: 229px; }
  .flap { position: absolute; border-radius: 0 0 22px 22px; }
  .flap-black { left: 8px; top: 0; width: 490px; height: 70px; background: var(--ink); clip-path: polygon(0 0, 100% 0, 98% 100%, 2% 100%); border-radius: 0 0 24px 24px; }
  .flap-black .wordmark { left: 196px; top: 26px; }
  .envelope-open { left: 593px; top: 277px; width: 506px; height: 230px; }
  .flap-blue { left: 0; top: 0; width: 506px; height: 71px; background: var(--brand-blue); clip-path: polygon(0 0, 100% 0, 98% 100%, 2% 100%); border-radius: 0 0 24px 24px; }
  .flap-blue .wordmark { left: 203px; top: 25px; }
  .envelope-front { left: 593px; top: 539px; width: 507px; height: 230px; }
  .envelope-front .wordmark { left: 30px; top: 33px; }
</style>
</head>
<body>

<section class="sheet letterhead" aria-label="Letterhead">
  <div class="wordmark"><span class="name">Fernhallow</span><span class="tag">Outdoor Advertising</span></div>
  <p class="salutation">Dear Mr. Pemberton,</p>
  <div class="letter-body">
    <p>Thank you for meeting with our team last week to discuss outdoor campaigns for the coming season. We have reviewed your goals and prepared a plan that places your message on high traffic routes across the city, with bright boards chosen for clear daytime and night viewing.</p>
    <p>Our crew handles every step, from design review and permits to printing, installation and upkeep. Each board is checked each month, and you will receive photo reports with simple notes on condition, lighting and placement so you always know how your space looks.</p>
    <p>We also offer flexible terms for short runs and seasonal promotions. Rates depend on location, size and length of the contract, and we are happy to bundle several faces into one package at a reduced price. Sample layouts and a full map of open sites are included with this letter for your review, and our staff can walk you through each option in person.</p>
    <p>Please let us know which locations interest you most, and we will hold them while you decide. We look forward to helping your brand stand tall along the roads your customers travel every day.</p>
  </div>
  <p class="closing">Sincerely,</p>
  <div class="signature" role="img" aria-label="Handwritten signature of Dale Fernhallow"></div>

  <div class="rule" style="left:44px; top:627px; width:418px;"><span class="blue" style="width:295px;"></span><span class="black"></span></div>
  <ul class="contact" style="left:44px; top:641px;">
    <li><svg viewBox="0 0 10 10"><path d="M2 0.5 L4 2.8 L3 4 Q4.3 6 6 7 L7.2 6 L9.5 8 L8.2 9.5 Q3.5 9 0.5 1.8 Z"/></svg>555-862-1907</li>
    <li><svg viewBox="0 0 10 10"><path d="M0 2 H10 V8.5 H0 Z M0.6 2.4 L5 5.8 L9.4 2.4" stroke="#fff" stroke-width="0.8"/></svg>dale@fernhallowsigns.example</li>
    <li><svg viewBox="0 0 10 10"><circle cx="5" cy="5" r="4.6"/><path d="M5 0.5 V9.5 M0.5 5 H9.5 M5 0.5 Q2 5 5 9.5 M5 0.5 Q8 5 5 9.5" stroke="#fff" stroke-width="0.6" fill="none"/></svg>fernhallowsigns.example</li>
  </ul>
  <div class="address" style="right:41px; top:641px;">
    <div class="company">Fernhallow Outdoor Advertising</div>
    <div>4873 Quarry Rd. 915 N. PO BOX 528617</div>
    <div>Austin, TX 78519</div>
  </div>
</section>

<section class="sheet envelope-back" aria-label="Envelope back, black flap">
  <div class="flap flap-black">
    <div class="wordmark small on-dark"><span class="name">Fernhallow</span><span class="tag">Outdoor Advertising</span></div>
  </div>
</section>

<section class="sheet envelope-open" aria-label="Envelope back, blue flap">
  <div class="flap flap-blue">
    <div class="wordmark small on-dark"><span class="name">Fernhallow</span><span class="tag">Outdoor Advertising</span></div>
  </div>
</section>

<section class="sheet envelope-front" aria-label="Envelope front">
  <div class="wordmark"><span class="name">Fernhallow</span><span class="tag">Outdoor Advertising</span></div>
  <div class="rule" style="left:30px; top:150px; width:441px;"><span class="blue" style="width:319px;"></span><span class="black"></span></div>
  <ul class="contact" style="left:30px; top:164px;">
    <li><svg viewBox="0 0 10 10"><path d="M2 0.5 L4 2.8 L3 4 Q4.3 6 6 7 L7.2 6 L9.5 8 L8.2 9.5 Q3.5 9 0.5 1.8 Z"/></svg>555-862-1907</li>
    <li><svg viewBox="0 0 10 10"><path d="M0 2 H10 V8.5 H0 Z M0.6 2.4 L5 5.8 L9.4 2.4" stroke="#fff" stroke-width="0.8"/></svg>dale@fernhallowsigns.example</li>
    <li><svg viewBox="0 0 10 10"><circle cx="5" cy="5" r="4.6"/><path d="M5 0.5 V9.5 M0.5 5 H9.5 M5 0.5 Q2 5 5 9.5 M5 0.5 Q8 5 5 9.5" stroke="#fff" stroke-width="0.6" fill="none"/></svg>fernhallowsigns.example</li>
  </ul>
  <div class="address" style="right:36px; top:164px;">
    <div class="company">Fernhallow Outdoor Advertising</div>
    <div>4873 Quarry Rd. 915 N. PO BOX 528617</div>
    <div>Austin, TX 78519</div>
  </div>
</section>

</body>
</html>
```